Business Card - Professional Minimalist - Double sided

We appreciate minimalist logo/web/collateral designs that allow design to tell a story. We want to relay a professional image/approach but throwing in a splash of modern when we’re able so long as it’s not distracting. Think 75% classic corporate, 25% modern. Open to black or white design, not sure which might look the best.

Target Market(s)

Senior executives or related government affairs contacts within the agriculture, energy, and defense industries (i.e., potential clients) but located outside of Washington, DC. Most potential clients based in DC with be familiar with both of us and our shared history.

Industry/Entity Type

Consulting

Contact Information for Business Card

Name: Daniel R. Whitlock
Title: Co-Founder & Partner
Address: 418 Bramblewood Ave. SE | Suite 2716 | Washington, D.C. 20019
Phone: (202) 555-0187
Email: Daniel@HollerbyWhitlock.com

Font styles to use
Serif

Colors

Designer to choose only greyscale colors for use in the design.

Requirements
Must have
• Name: Daniel R. Whitlock
Phone: (202) 555-0187

```html
<!DOCTYPE html>
<html lang="en">
<head>
<meta charset="utf-8">
<title>Hollerby Whitlock Group – Business Card</title>
<link href="https://fonts.googleapis.com/css2?family=Tinos:wght@400;700&display=swap" rel="stylesheet">
<style>
  :root {
    --stage: #d9d9d9;
    --ink-black: #1f1b1c;
    --paper: #ffffff;
    --paper-shade: #eeeeee;
    --silver: #9a9a9a;
    --silver-light: #c4c4c4;
    --text-dark: #3a3a3a;
    --text-mid: #5a5a5a;
    --icon-grey: #a8a8a8;
  }
  * { box-sizing: border-box; margin: 0; padding: 0; }
  html, body {
    width: 1200px; height: 880px; overflow: hidden;
    background: var(--stage);
    font-family: "Tinos", "Times New Roman", serif;
  }
  .stage {
    width: 1200px; height: 880px;
    display: flex; flex-direction: column; align-items: center; justify-content: center;
    gap: 28px;
  }
  .card {
    position: relative;
    width: 600px; height: 343px;
    box-shadow: 0 6px 18px rgba(0,0,0,.25);
    overflow: hidden;
  }
  /* Back side */
  .card--back {
    background: var(--ink-black);
    display: flex; align-items: center; justify-content: center; gap: 12px;
  }
  .card--back .brand-mark {
    width: 20px; height: 20px; border: 2px solid var(--silver-light);
  }
  .card--back .brand-name {
    color: var(--silver-light);
    font-size: 22px; letter-spacing: 3px; text-transform: uppercase;
  }
  /* Front side */
  .card--front {
    background: linear-gradient(180deg, var(--paper) 55%, var(--paper-shade) 100%);
  }
  .front-band { position: absolute; left: 0; top: 0; }
  .brand-lockup {
    position: absolute; left: 58px; top: 104px;
    display: inline-grid; grid-template-columns: auto auto;
    column-gap: 12px; align-items: center;
  }
  .brand-lockup .brand-mark {
    grid-row: 1 / span 2; width: 26px; height: 26px; border: 2px solid var(--silver);
  }
  .brand-lockup .brand-name {
    color: var(--silver);
    font-size: 28px; line-height: 30px; letter-spacing: 1.5px; text-transform: uppercase;
    white-space: nowrap;
  }
  .brand-sub {
    display: flex; align-items: center; gap: 10px; margin-top: 2px;
  }
  .brand-sub .brand-rule { flex: 1; height: 1px; background: var(--silver); }
  .brand-sub .brand-suffix {
    color: var(--silver); font-size: 12px; letter-spacing: 6px; text-transform: uppercase;
    margin-right: -6px;
  }
  .contact-person { position: absolute; left: 50px; top: 222px; }
  .person-name {
    font-weight: 700; font-size: 18px; color: var(--text-dark);
    text-transform: uppercase; letter-spacing: .5px;
  }
  .person-title {
    font-size: 11px; color: var(--text-mid); text-transform: uppercase;
    letter-spacing: .5px; margin-top: 2px;
  }
  .person-rule { width: 230px; height: 1px; background: var(--silver); margin: 10px 0 8px; }
  .contact-line {
    display: flex; align-items: center; gap: 8px;
    font-size: 13px; color: var(--text-mid); line-height: 20px;
  }
  .contact-icon { width: 13px; height: 13px; flex: none; }
  .contact-address {
    position: absolute; right: 38px; top: 200px; text-align: right;
    font-size: 12px; color: var(--text-mid); line-height: 17px;
  }
  .address-rule {
    display: flex; align-items: center; gap: 8px; justify-content: flex-end; margin-bottom: 6px;
  }
  .address-rule span { width: 250px; height: 1px; background: var(--silver); }
</style>
</head>
<body>
<main class="stage">
  <section class="card card--back" aria-label="Card back">
    <span class="brand-mark"></span>
    <span class="brand-name">Hollerby Whitlock Group</span>
  </section>

  <section class="card card--front" aria-label="Card front">
    <svg class="front-band" width="600" height="343" viewBox="0 0 600 343" aria-hidden="true">
      <path d="M0 28 H470 A60 60 0 0 1 530 88 V190 H0 Z" fill="var(--ink-black)"/>
    </svg>
    <div class="brand-lockup">
      <span class="brand-mark"></span>
      <span class="brand-name">Hollerby Whitlock</span>
      <div class="brand-sub">
        <span class="brand-rule"></span>
        <span class="brand-suffix">Group</span>
      </div>
    </div>

    <div class="contact-person">
      <div class="person-name">Daniel R. Whitlock</div>
      <div class="person-title">Co-Founder &amp; Partner</div>
      <div class="person-rule"></div>
      <div class="contact-line">
        <svg class="contact-icon" viewBox="0 0 14 14"><rect width="14" height="14" rx="3" fill="var(--icon-grey)"/><path d="M4 3.5l1.6-.4 1 2-1 .8a6 6 0 0 0 2.5 2.5l.8-1 2 1-.4 1.6C8 10.5 3.5 6 4 3.5z" fill="#fff"/></svg>
        <span>(202) 555-0187</span>
      </div>
      <div class="contact-line">
        <svg class="contact-icon" viewBox="0 0 14 14"><rect width="14" height="14" rx="3" fill="var(--icon-grey)"/><rect x="3" y="4.5" width="8" height="5.5" fill="#fff"/><path d="M3 4.5l4 3 4-3" stroke="var(--icon-grey)" fill="none" stroke-width=".9"/></svg>
        <span>Daniel@HollerbyWhitlock.com</span>
      </div>
    </div>

    <div class="contact-address">
      <div class="address-rule">
        <span></span>
        <svg class="contact-icon" viewBox="0 0 14 14"><rect width="14" height="14" rx="3" fill="var(--icon-grey)"/><path d="M7 2.5a3 3 0 0 1 3 3c0 2.2-3 5.5-3 5.5S4 7.7 4 5.5a3 3 0 0 1 3-3z" fill="#fff"/><circle cx="7" cy="5.5" r="1.1" fill="var(--icon-grey)"/></svg>
      </div>
      <div>418 Bramblewood Ave. SE</div>
      <div>Suite 2716, Washington, D.C. 20019</div>
    </div>
  </section>
</main>
</body>
</html>
```